business card for author of crime novel

I am an author with a new book. I need a business card with the book's cover on one side (already uploaded), and contact details on the other.

Walt Pemberty
Author

telephone: 646-512-7380
website: www.waltpemberty.net
facebook: facebook.com/wpemberty
twitter: twitter.com/wpemberty
email: wpemberty@postvale.net

Target Market(s)

Readers of mystery books

Industry/Entity Type

Business

Contact Information for Business Card

Walt Pemberty
Author

telephone: 646-512-7380

Font styles to use
Serif
Sans Serif

Requirements
Must have
• Book cover on one side. My contact info on the other, with the name of the book repeated if that makes sense. Clean design.
Should not have
• Overly ornate, too formal, too distracting

```html
<!DOCTYPE html>
<html lang="en">
<head>
<meta charset="utf-8">
<title>Walt Pemberty – Author Business Card</title>
<link rel="stylesheet" href="https://fonts.googleapis.com/css2?family=Old+Standard+TT:wght@700&family=Cinzel:wght@400&family=Gelasio:wght@400&family=Open+Sans:wght@400&display=swap">
<style>
  :root {
    --page-bg: #ececec;
    --card-stock: #cfdbe1;
    --cover-gold: #dfa12a;
    --cover-gold-dark: #c98a18;
    --title-ink: #1f1a12;
    --photo-light: #9fb4bf;
    --photo-dark: #3c4f5a;
    --byline: #d4e64a;
    --label-paper: #e8cf9c;
    --label-ink: #3a2a14;
    --panel-slate: #374851;
    --name-white: #ffffff;
    --contact-grey: #c3ccd1;
  }
  * { box-sizing: border-box; margin: 0; padding: 0; }
  html, body { width: 1200px; height: 800px; overflow: hidden; }
  body {
    background: var(--page-bg);
    display: flex;
    align-items: center;
    justify-content: center;
    gap: 90px;
  }
  .card {
    width: 320px;
    height: 540px;
    background: var(--card-stock);
    padding: 26px 24px;
    box-shadow: 0 2px 6px rgba(0,0,0,0.15);
  }

  /* Front: book cover */
  .book-cover {
    height: 100%;
    background: var(--cover-gold);
    padding: 16px 18px;
    position: relative;
    display: flex;
    flex-direction: column;
  }
  .book-title {
    font-family: "Old Standard TT", serif;
    font-weight: 700;
    font-size: 22px;
    letter-spacing: 1px;
    color: var(--title-ink);
    text-align: right;
    margin-bottom: 12px;
  }
  .cover-photo {
    flex: 1;
    background: linear-gradient(160deg, var(--photo-light) 0%, #6f8795 45%, var(--photo-dark) 100%);
    position: relative;
  }
  .byline {
    position: absolute;
    right: 14px;
    bottom: 58px;
    font-family: "Cinzel", serif;
    font-size: 19px;
    line-height: 1.05;
    color: var(--byline);
    text-align: right;
    letter-spacing: 1px;
  }
  .series-label {
    position: absolute;
    left: 6px;
    bottom: 30px;
    background: var(--label-paper);
    color: var(--label-ink);
    font-family: "Old Standard TT", serif;
    font-weight: 700;
    font-size: 14px;
    padding: 6px 14px;
    border-radius: 3px;
    box-shadow: 0 1px 3px rgba(0,0,0,0.35);
  }

  /* Back: contact details */
  .contact-panel {
    height: 100%;
    background: var(--panel-slate);
    padding: 190px 30px 0;
  }
  .author-name {
    font-family: "Gelasio", serif;
    font-size: 27px;
    color: var(--name-white);
    line-height: 1.15;
  }
  .author-role {
    font-family: "Gelasio", serif;
    font-size: 25px;
    color: var(--name-white);
    margin-bottom: 16px;
  }
  .contact-list {
    list-style: none;
    font-family: "Open Sans", sans-serif;
    font-size: 15px;
    line-height: 1.45;
    color: var(--contact-grey);
  }
</style>
</head>
<body>
  <section class="card card-front">
    <div class="book-cover">
      <h1 class="book-title">DEAD END ALLEY</h1>
      <div class="cover-photo" role="img" aria-label="Photograph of an old city apartment building with fire escapes, in cold blue tones"></div>
      <p class="byline">WALT<br>PEMBERTY</p>
      <p class="series-label">A Hollis Crane Mystery</p>
    </div>
  </section>

  <section class="card card-back">
    <div class="contact-panel">
      <h2 class="author-name">Walt Pemberty</h2>
      <p class="author-role">Author</p>
      <ul class="contact-list">
        <li>646-512-7380</li>
        <li>www.waltpemberty.net</li>
        <li>facebook.com/wpemberty</li>
        <li>twitter.com/wpemberty</li>
        <li>wpemberty@postvale.net</li>
      </ul>
    </div>
  </section>
</body>
</html>
```